Thai Menu Design Project

We need a new menu design for a Thai restaurant in Fort Worth, Texas. We are a family-owned and really proud about our food and our service. We want the menu to feel healthy, modern, delicious, artistic Thai, and friendly. The colors we used in our restaurant are maroon, burgundy, black, white, gold and pale yellow.

Please look at our website www.kavonbrisket.com
for the reference of the menus and the photos we use.

The menu can be in any number of pages (the fewer the better though) The size of the paper is US letter.
Updates

Update:

- We don't put the photos of the food in the menu pages anymore, instead, we like to put the photos of the herbs and their benefits (found in the file 'herb benefits') on the menu pages instead.

- the paper size is US letter.

- we don't have specific numbers of pages but the fewer the better

Thank you!

I added logos and background photo again in case the previous files did not work. Thanks!

Target Market(s)

Trendy socialized people from 20-30s,couples of all ages from 20s-60s,and families.

Industry/Entity Type

Restaurant

Requirements
Must have
• We want the menu to feel healthy, modern, delicious, artistic, Thai, and friendly.

We like to keep the colors maroon, burgundy, black, gold, pale yellow, and off white.

We like to put the photos of the herbs and their benefits (available in the file called 'herb benefits') randomly in the menu pages.

*Please use the photos available in the file called 'herb benefits' along with its details somewhere in the pages. You can change the photo of each herb to the ones you find more fitting from the internet.

Nice to have
• If we can add the wallpaper pattern in our menu it will be great. It can be used in anyway.

```html
<!DOCTYPE html>
<html lang="en">
<head>
<meta charset="utf-8">
<title>Herbs Benefits – Menu Spread</title>
<link rel="stylesheet" href="https://fonts.googleapis.com/css2?family=Cormorant+Garamond:ital,wght@1,500&family=PT+Sans:ital,wght@0,400;1,700&display=swap">
<style>
  :root {
    --charcoal: #262626;
    --charcoal-light: #343434;
    --maroon: #4a1530;
    --maroon-deep: #2e0c1d;
    --gold: #9c7a3c;
    --paper: #efeee8;
    --ink: #2b2b2b;
    --ring: #ffffff;
  }
  * { margin: 0; padding: 0; box-sizing: border-box; }
  html, body { width: 1200px; height: 776px; overflow: hidden; }
  body { background: var(--charcoal); }
  .spread {
    position: relative; width: 1200px; height: 776px; overflow: hidden;
    background: radial-gradient(ellipse at 50% 40%, var(--charcoal-light), var(--charcoal) 70%);
  }
  .wallpaper-band {
    position: absolute; left: 0; top: 0; width: 1200px; height: 48px;
    background: linear-gradient(90deg, var(--maroon) 0%, #5a2038 25%, var(--maroon) 50%, #5a2038 75%, var(--maroon) 100%);
    border-bottom: 2px solid var(--maroon-deep);
  }
  .wallpaper-strip {
    position: absolute; top: 738px; height: 14px;
    background: linear-gradient(90deg, var(--maroon), #6a2a40, var(--maroon));
  }
  .page {
    position: absolute; top: 45px; width: 305px; height: 693px;
    background: var(--paper);
    box-shadow: 0 0 12px rgba(0,0,0,.5);
  }
  .page--left { left: 155px; }
  .page--right { left: 738px; }
  .page-title {
    position: absolute; top: 42px;
    font-family: "Cormorant Garamond", serif; font-style: italic; font-weight: 500;
    font-size: 21px; color: var(--ink);
  }
  .page--left .page-title { left: 22px; }
  .page--right .page-title { right: 20px; }
  .herb {
    position: absolute; left: 22px; width: 263px;
    font-family: "PT Sans", sans-serif; font-size: 6.3px; line-height: 8.6px; color: var(--ink);
  }
  .herb h2 {
    font-family: "PT Sans", sans-serif; font-style: italic; font-weight: 700;
    font-size: 6.8px; margin-bottom: 8px;
  }
  .herb p { text-align: justify; margin-bottom: 8px; }
  .herb--end h2 { text-align: right; }
  .herb--end p { text-align-last: right; }
  .photo {
    position: absolute; border-radius: 50%; border: 5px solid var(--ring);
    box-shadow: 0 2px 6px rgba(0,0,0,.45);
  }
  .boat { position: absolute; border-radius: 50% / 12%; box-shadow: 0 4px 10px rgba(0,0,0,.5); }
</style>
</head>
<body>
<main class="spread">
  <div class="wallpaper-band" role="img" aria-label="Maroon and gold damask wallpaper pattern band"></div>
  <div class="wallpaper-strip" style="left:155px;width:305px" role="img" aria-label="Maroon damask pattern strip"></div>
  <div class="wallpaper-strip" style="left:738px;width:305px" role="img" aria-label="Maroon damask pattern strip"></div>

  <section class="page page--left">
    <h1 class="page-title">Herbs benefits</h1>

    <article class="herb" style="top:83px">
      <h2>Galangal</h2>
      <p>Commonly known as ‘Siamese ginger’, the name galangal is derived form the Chinese word for ginger. Galangal contains anti-inflammatory properties which is beneficial in treatment of arthritis and rheumatoid arthritis. Galangal contains a host of anti-oxidants that helps to minimise the damage caused by free radicals and other toxins in the body. To improve blood circulation in the body, include galangal in your diet.</p>
    </article>

    <article class="herb herb--end" style="top:176px">
      <h2>Basil</h2>
      <p>The king of herbs, basil is one of the oldest and popular herbal plants. This highly prized plant is revered as “holy herb” in many traditions all around the world. The name “basil” comes from the ancient Greek word basilikohn, meaning “royal”. Basil is originally native to Iran, India and other tropical regions of Asia. This herbal plant is grown for its medicinally useful leaves and seeds.</p>
      <p>Its oils and extracts are said to have antioxidant and antibacterial properties. Other benefits of basil include cancer prevention, skin and hair health, bone and connective tissue, digestive tract health, anti-bacterial, immune system.</p>
    </article>

    <article class="herb" style="top:300px">
      <h2>Lemongrass</h2>
      <p>Its name gives away the basics -- this is a grass with a lemony taste. Lemongrass has many anti-oxidant and disease preventing properties such as vitamin C, vitamin A, potassium, zinc, calcium, iron, manganese, copper, and magnesium. Lemongrass oil when used in aromatherapy restores and revitalizes the whole body, helping to relieve the symptoms of headaches, body-aches, nervous exhaustion and stress-related conditions.</p>
      <p>Many people use lemongrass as a calmative agent; to help them deal with anxiety and nervousness People who suffer from Insomnia report its ability to help them rest and sleep deeply.</p>
    </article>

    <article class="herb herb--end" style="top:456px">
      <h2>Kaffir leaves</h2>
      <p>The kaffir lime is sometimes referred to as “Thai limes” or “wild limes”. The leaves, zest and juice of the kaffir lime are so commonly used to impart an aromatic and astringent flavor in a wide variety of Thai dishes from soups and salads to curries and stir-fried dishes. The fruit has essential oils, which are incorporated into various ointments as well. For its benefits, the rind itself serves as an ingredient in many medicinal tonics believed to be beneficial for the blood. Just like galangal and lemon grass, the rind of the lime is also said to be beneficial for digestion.</p>
    </article>

    <article class="herb" style="top:529px">
      <h2>Fingerroot</h2>
      <p>In English, the root has traditionally been called Fingerroot because the shape of the rhizome resembles that of fingers growing out of a centerpiece. Ginger key is used in China only for its medicinal properties, whereas in Thailand it is cultivated for culinary and medicinal purposes. It has a pungent flavor and spicy, peppery taste spicy is eaten as a vegetable and used as a spice.</p>
      <p>The root contains health benefiting essential oils that help improve the intestinal motility and have been anti-inflammatory, painkiller (analgesic), nerve soothing, anti-pyretic as well as anti-bacterial properties. Studies have shown that it may reduce nausea induced by motion sickness or pregnancy and may help relieve migraine headache.</p>
    </article>
  </section>

  <section class="page page--right">
    <h1 class="page-title">Herbs benefits</h1>

    <article class="herb herb--end" style="top:83px">
      <h2>Lime</h2>
      <p>The first fruit that comes to mind when it comes to medicinal uses is perhaps the good old lime. The lime is the sweeter cousin of the lemon. Limes are packed with vitamin C. Fresh or from concentrate, lime juice contains more citric acid than orange or grapefruit juice. Limes are good for women’s health. These citrus gems contain calcium and folate, two nutrients that are important for post-menopausal women and women of child-bearing age. Limes are anti-carcinogenic. The limonoid compounds in limes have been shown to prevent cancers of the colon, stomach and blood. Lime juice can help prevent formation of kidney stones.</p>
    </article>

    <article class="herb" style="top:189px">
      <h2>Chili</h2>
      <p>The Health benefits of eating chilies are well documented but surprisingly little known, Chili can aid, relieve and prevent many conditions. Eating chilies can have a very positive impact on people that are overweight or suffer from diabetes. The study carried out yielded that the normal eating of chilies can help significantly control insulin levels after eating a meal. Chilies can have a dramatic impact on your health by helping to boost circulation and also act as a thinner to help protect against strokes.</p>
      <p>Chilies are great at quickly and effectively opening your nasal passages, allowing you to breathe more easily, no doubt you would have noticed the almost immediate relief of congestion, after eating a good hot curry if you have a cold.</p>
    </article>

    <article class="herb herb--end" style="top:321px">
      <h2>Garlic</h2>
      <p>Garlic is one of the most valuable and versatile foods on the planet. Builders of the ancient pyramids were said to eat garlic daily for enhanced endurance and strength. Roman emperors couldn’t eat enough of it, as it was considered an antidote to poisons which were very popular in certain political circles of the time. Today garlic is a widely recognized health enhancing supplement. Garlic promotes the well-being of the heart and immune systems with antioxidant properties and helps maintain healthy blood circulation. Another benefit of garlic is it helps regulate the body’s blood pressure.</p>
      <p>So whether you have problems with low or high blood pressure, garlic can help equalize it. In addition to all these health benefits, garlic is packed with vitamins and nutrients. Some of these include protein, potassium, Vitamins A, B, B2 and C, Calcium, Zinc and many others.</p>
    </article>

    <article class="herb" style="top:461px">
      <h2>Glass Noodle</h2>
      <p>Glass noodles, which are also known as bean thread, vermicelli, or cellophane noodles, are a staple in Thai and other Asian cooking, where they are both boiled and stir-fried. With their bland taste, glass noodles are an excellent addition to flavorful, saucy dishes because they will readily pick up the flavor of broths and sauces.</p>
    </article>

    <article class="herb herb--end" style="top:545px">
      <h2>Shiratake Noodle</h2>
      <p>The famous noodle seen in several health magazines. The Japanese have a noodle by the name of shiratake that’s made from a type of yam that’s packed with dietary fiber but has no carbohydrates. These low-carb noodles can satisfy your spaghetti cravings, and are a gluten free replacement for pasta. Shiratake Noodles are made from the root of a very special type of plant in Asian, and are naturally low in calories and carbs, plus they are an excellent source of fiber. If you are a health-conscious eater then Sh</p>
    </article>
  </section>

  <div class="photo" style="left:55px;top:82px;width:108px;height:108px;background:radial-gradient(circle,#e3d7b4,#b79f6c)" role="img" aria-label="Photo of galangal roots"></div>
  <div class="photo" style="left:55px;top:318px;width:108px;height:108px;background:radial-gradient(circle,#e6e3c2,#7b8f4a)" role="img" aria-label="Photo of lemongrass stalks"></div>
  <div class="photo" style="left:55px;top:545px;width:108px;height:108px;background:radial-gradient(circle,#d9b07a,#9b6a3a)" role="img" aria-label="Photo of fingerroot rhizomes"></div>
  <div class="photo" style="left:458px;top:188px;width:108px;height:108px;background:radial-gradient(circle,#6fa33a,#2f5a1c)" role="img" aria-label="Photo of fresh basil leaves"></div>
  <div class="photo" style="left:458px;top:430px;width:108px;height:108px;background:radial-gradient(circle,#6a9d3e,#8a6a3e)" role="img" aria-label="Photo of kaffir lime leaves in a bowl"></div>
  <div class="photo" style="left:636px;top:208px;width:108px;height:108px;background:radial-gradient(circle,#d23a2a,#7a1a12)" role="img" aria-label="Photo of red chilies"></div>
  <div class="photo" style="left:636px;top:430px;width:108px;height:108px;background:radial-gradient(circle,#dfe6ea,#8a9aa2)" role="img" aria-label="Photo of glass noodles"></div>
  <div class="photo" style="left:1036px;top:90px;width:108px;height:118px;background:radial-gradient(circle,#8fcf3a,#3f7a18)" role="img" aria-label="Photo of fresh limes"></div>
  <div class="photo" style="left:1036px;top:340px;width:108px;height:115px;background:radial-gradient(circle,#f2efe6,#b8b1a0)" role="img" aria-label="Photo of garlic bulbs"></div>
  <div class="photo" style="left:1036px;top:550px;width:108px;height:112px;background:radial-gradient(circle,#f4f1ea,#c9c2b3)" role="img" aria-label="Photo of shiratake noodles"></div>

  <div class="boat" style="left:70px;top:620px;width:70px;height:200px;transform:rotate(-38deg);background:linear-gradient(180deg,#3a3a32,#8a9a2a 40%,#5a5a2a)" role="img" aria-label="Floating market boat loaded with limes"></div>
  <div class="boat" style="left:460px;top:560px;width:80px;height:250px;transform:rotate(28deg);background:linear-gradient(180deg,#3a3a32,#9aa52a 35%,#cfc6a8 70%,#4a4630)" role="img" aria-label="Floating market boat with fruit and a straw hat"></div>
  <div class="boat" style="left:650px;top:510px;width:85px;height:280px;transform:rotate(-14deg);background:linear-gradient(180deg,#3a3a32,#b3403a 25%,#9aa52a 50%,#cfc6a8 75%,#4a4630)" role="img" aria-label="Floating market boat with a vendor and limes"></div>
  <div class="boat" style="left:1045px;top:620px;width:70px;height:210px;transform:rotate(38deg);background:linear-gradient(180deg,#3a3a32,#8a9a2a 40%,#5a5a2a)" role="img" aria-label="Floating market boat loaded with limes"></div>
</main>
</body>
</html>
```